Kerno Solutions: searching for a flyer to trow in letterboxes for properties we are interested in

Hello ,

Introduction:
We are a company based in Luxembourg called "Kerno Solutions". We are specialized in buying properties on which we develop and build constructions before selling them.

Informations for the flyer:
We need a flyer to trow into the letter boxes of property owners letting them know that we are interested in buying their property, if they are interested they can give us a call.

The text for the flyer/letter is in the attachment called >>2020-03-11_KS_Text for flyer,letter there might be slight changes<<.

We need to look competent, professional and financially stable.

The flyer needs to be short and not over welling with information otherwise it will land in the trash.

We have decided that we don't want real pictures on the flyer, but shapes of any kind, blue prints, drawings are fine.

Format should be in DIN A4. We plan to print the flyer on both sides in two different languages, in other words the design will be the same on both sides only the text will be in a different language.

I also added our current logo and here is the design of the website that is under construction at the moment http://www.kernosolutions-example.lu/. The logo's color can be changed into a different blue or uni color (all white or all black).
Updates

Hi, First time user the howl thing started faster as expected. Furthermore, I need to catch my boss to discust the project with him and he is on a lot of meetings. Please give us a little bit more time. Thanks

Target Market(s)

Property owners

Requirements
Must have
• email, phone number, tax number (RCS), Tax number , matriculation and address.
see word file in attachment for information
Nice to have
• Our company logo, in one form or an other, you can be creative, the logo is in the attachment.
Should not have
• Real pictures

```html
<!DOCTYPE html>
<html lang="fr">
<head>
<meta charset="utf-8">
<title>Kerno Solutions – Flyer</title>
<link rel="stylesheet" href="https://fonts.googleapis.com/css2?family=Oswald:wght@600&family=Shadows+Into+Light+Two&family=Tinos:wght@400;700&family=Mrs+Saint+Delafield&family=Lato:wght@400;700&display=swap">
<style>
  :root {
    --stage: #e9eaec;
    --paper: #ffffff;
    --letter-bg: #f8f9fa;
    --brand-blue: #24557f;
    --ink: #1f1f1f;
    --ink-soft: #2a2a2a;
    --header-tone-a: #dfe6ee;
    --header-tone-b: #2f6fae;
    --footer-tone-a: #ffffff;
    --footer-tone-b: #cdd6e0;
  }
  * { margin: 0; padding: 0; box-sizing: border-box; }
  html, body { width: 898px; height: 1200px; overflow: hidden; background: var(--stage); }
  .flyer {
    position: absolute; left: 25px; top: 0;
    width: 848px; height: 1200px;
    background: var(--paper); overflow: hidden;
  }
  .header {
    position: absolute; left: 0; top: 0; width: 848px; height: 400px;
    background: linear-gradient(90deg, #f1f3f5 0%, #f5f6f8 100%);
  }
  .header-visual {
    position: absolute; left: 0; top: 0; width: 480px; height: 400px;
    background:
      radial-gradient(ellipse at 55% 55%, var(--header-tone-b) 0%, rgba(47,111,174,0.55) 35%, rgba(241,243,245,0) 70%),
      linear-gradient(135deg, #9aa3ad 0%, var(--header-tone-a) 45%, #f1f3f5 100%);
  }
  .site-url {
    position: absolute; left: 589px; top: 68px;
    font: 400 17px/1 "Lato", sans-serif; letter-spacing: 1px; color: var(--ink-soft);
  }
  .site-url .accent { color: var(--brand-blue); }
  .brand {
    position: absolute; display: flex; align-items: center;
    font-family: "Oswald", sans-serif; font-weight: 600; color: var(--brand-blue);
    text-transform: uppercase; line-height: 1;
  }
  .brand-square { background: var(--brand-blue); flex: none; }
  .brand--large { left: 470px; top: 240px; font-size: 40px; gap: 14px; }
  .brand--large .brand-square { width: 34px; height: 34px; }
  .brand--small { left: 86px; top: 898px; font-size: 17px; gap: 7px; }
  .brand--small .brand-square { width: 14px; height: 14px; }

  .letter {
    position: absolute; left: 0; top: 400px; width: 848px; height: 400px;
    background: var(--letter-bg);
  }
  .salutation {
    position: absolute; left: 86px; top: 48px;
    font: 700 21px/1 "Tinos", serif; color: var(--ink);
  }
  .body-text {
    position: absolute; left: 86px; width: 680px;
    font: 400 20px/29px "Shadows Into Light Two", cursive; color: var(--ink);
  }
  .p1 { top: 87px; line-height: 32px; }
  .p2 { top: 164px; line-height: 27px; }
  .p3 { top: 229px; line-height: 27px; }
  .closing {
    position: absolute; left: 86px; top: 302px;
    font: 400 30px/1 "Mrs Saint Delafield", cursive; color: var(--ink);
  }
  .team {
    position: absolute; left: 86px; top: 346px;
    font: 400 16px/1 "Tinos", serif; color: var(--brand-blue);
  }

  .footer {
    position: absolute; left: 0; top: 800px; width: 848px; height: 400px; background: var(--paper);
  }
  .footer-visual {
    position: absolute; left: 336px; top: 0; width: 512px; height: 400px;
    background:
      linear-gradient(200deg, var(--footer-tone-b) 0%, #e8edf2 40%, rgba(255,255,255,0) 75%),
      var(--footer-tone-a);
  }
  .company-name {
    position: absolute; left: 86px; top: 180px;
    font: 400 19px/1 "Lato", sans-serif; color: var(--brand-blue);
  }
  .company-rule {
    position: absolute; left: 86px; top: 210px; width: 18px; height: 3px; background: var(--brand-blue);
  }
  .contact-list { position: absolute; left: 84px; top: 230px; list-style: none; }
  .contact-list li {
    display: flex; align-items: center; height: 27.5px;
    font: 400 16px/1 "Lato", sans-serif; color: var(--ink);
  }
  .contact-icon { width: 12px; height: 12px; margin-right: 6px; flex: none; }
  .contact-list .no-icon { padding-left: 18px; }
</style>
</head>
<body>
<div class="flyer">
  <header class="header">
    <div class="header-visual" role="img" aria-label="Photo d'un bureau d'architecte : ordinateur portable, plan bleu, lunettes, mètre ruban, crayon et plante"></div>
    <p class="site-url">www.<span class="accent">KernoSolutions-example</span>.lu</p>
    <div class="brand brand--large"><span class="brand-square"></span>Kerno Solutions</div>
  </header>

  <section class="letter">
    <p class="salutation">Madame, Monsieur,</p>
    <p class="body-text p1">Ce courrier vous a été adressé, car votre propriété a attiré notre attention. Nous souhaiterions discuter avec vous de son éventuel rachat par notre société.</p>
    <p class="body-text p2">En cas d'accord, nous vous assurons une décision rapide, un paiement garanti, et zéro frais d'intermédiaire.</p>
    <p class="body-text p3">En attendant de vos nouvelles, nous restons à votre entière disposition pour tout renseignement.</p>
    <p class="closing">Salutations distinguées,</p>
    <p class="team">L'équipe de Kerno Solutions</p>
  </section>

  <footer class="footer">
    <div class="footer-visual" role="img" aria-label="Photo de plans techniques avec rouleaux de papier, crayons et calculatrice"></div>
    <div class="brand brand--small" style="top:98px"><span class="brand-square"></span>Kerno Solutions</div>
    <p class="company-name">Kerno Solutions sàrl</p>
    <span class="company-rule"></span>
    <ul class="contact-list">
      <li><svg class="contact-icon" viewBox="0 0 12 12"><path d="M6 1a3 3 0 0 1 3 3c0 2.2-3 6-3 6S3 6.2 3 4a3 3 0 0 1 3-3z" fill="none" stroke="#24557f" stroke-width="1.2"/><circle cx="6" cy="4" r="1" fill="#24557f"/></svg>17 rue des Artisans, L-3290 Bettembourg</li>
      <li><svg class="contact-icon" viewBox="0 0 12 12"><rect x="1" y="3" width="10" height="7" fill="none" stroke="#24557f" stroke-width="1.1"/><path d="M1 3l5 4 5-4" fill="none" stroke="#24557f" stroke-width="1.1"/></svg>info@kernosolutions-example.lu</li>
      <li><svg class="contact-icon" viewBox="0 0 12 12"><circle cx="6" cy="6" r="5" fill="none" stroke="#24557f" stroke-width="1.1"/><path d="M4.2 3.5l1 1.2-.6.8a3.5 3.5 0 0 0 1.9 1.9l.8-.6 1.2 1-.8 1A4.8 4.8 0 0 1 3.2 4.3z" fill="#24557f"/></svg>691 000 482</li>
      <li class="no-icon">RCS : will be added</li>
      <li><svg class="contact-icon" viewBox="0 0 12 12"><circle cx="6" cy="6" r="5" fill="none" stroke="#24557f" stroke-width="1.1"/><ellipse cx="6" cy="6" rx="2.2" ry="5" fill="none" stroke="#24557f" stroke-width="0.9"/><path d="M1 6h10" stroke="#24557f" stroke-width="0.9"/></svg>www.kernosolutions-example.lu</li>
    </ul>
  </footer>
</div>
</body>
</html>
```